Fresh Business Card Designs Required

Looking to get new business cards but want a fresh look and feel. The logo has a large curved square which can be incorporated, or alternative the text-only version of the logo can be utilised if it is better. Looking for fresh ideas. I prefer flat designs, also incorporating a QR code to our contact us page on website would be great to make contact easy.
Updates

I have just uploaded the .ai files for our logo to make it easier to drop into your designs. Thanks for your consideration looking forward to seeing the results!

Target Market(s)

Generally business cards are handed to consumers who are contacting us for information.

Industry/Entity Type

Water Pumping and Irrigation, Water Filtration,

Contact Information for Business Card

Company Name / Logo, Name, Job Title, Phone No., Direct Line, Address

Font styles to use
Sans Serif

Colors
00AB8E
00BBA5
67D7C9
C6EFE9
E9F9F6
FFF300
FFF600
FEFA6F
FFFEC7
FFFEE8

Requirements
Must have
• Contact Details!!!! :)
Nice to have
• QR Code to contact us page, list of products (not critical!)

```html
<!DOCTYPE html>
<html lang="en">
<head>
<meta charset="utf-8">
<title>Tidewell Pumps – Business Card</title>
<link rel="stylesheet" href="https://fonts.googleapis.com/css2?family=Open+Sans:wght@400;600;800&display=swap">
<style>
  :root {
    --bg: #b6b6b6;
    --card-white: #ffffff;
    --green: #3fae49;
    --yellow: #f3de00;
    --yellow-deep: #ddce1c;
    --ink-grey: #8c8c8c;
    --rule-grey: #a9a9a9;
  }
  * { box-sizing: border-box; margin: 0; padding: 0; }
  html, body { width: 1200px; height: 848px; overflow: hidden; }
  body {
    background: var(--bg);
    font-family: "Open Sans", Arial, sans-serif;
    position: relative;
  }
  .card {
    position: absolute;
    top: 280px;
    width: 520px;
    height: 289px;
    border-radius: 30px;
    overflow: hidden;
  }
  .card--front { left: 45px; background: var(--card-white); }
  .card--back {
    left: 635px;
    background: radial-gradient(ellipse at 50% 45%, var(--yellow) 0%, var(--yellow-deep) 100%);
  }

  /* company name, one line, one weight, one colour */
  .company {
    display: flex;
    align-items: center;
    gap: 8px;
    color: var(--green);
    font-weight: 800;
    white-space: nowrap;
    line-height: 1;
  }
  .company__dot {
    width: 12px;
    height: 12px;
    border-radius: 50%;
    background: var(--green);
    flex: none;
  }

  /* front */
  .card--front .company {
    position: absolute;
    left: 30px;
    top: 131px;
    font-size: 24px;
  }
  .divider {
    position: absolute;
    left: 262px;
    top: 70px;
    width: 1px;
    height: 150px;
    background: var(--rule-grey);
  }
  .contact {
    position: absolute;
    left: 282px;
    top: 62px;
    color: var(--ink-grey);
    font-size: 13px;
    line-height: 1.35;
  }
  .contact__name {
    color: var(--green);
    font-weight: 800;
    font-size: 15px;
    letter-spacing: 0.5px;
    text-transform: uppercase;
  }
  .contact__role {
    font-size: 11px;
    letter-spacing: 1px;
    text-transform: uppercase;
    margin-bottom: 10px;
  }
  .contact__list { list-style: none; }
  .contact__item { display: flex; align-items: flex-start; gap: 10px; margin-bottom: 5px; }
  .contact__icon { width: 15px; height: 15px; flex: none; margin-top: 2px; fill: var(--green); }

  /* back */
  .card--back .company {
    position: absolute;
    left: 70px;
    top: 70px;
    font-size: 30px;
  }
  .services {
    position: absolute;
    left: 70px;
    top: 118px;
    width: 380px;
    display: flex;
    justify-content: space-between;
    color: var(--green);
    font-weight: 800;
    font-size: 15px;
    letter-spacing: 1.5px;
    text-transform: uppercase;
  }
  .products {
    position: absolute;
    left: 0;
    right: 0;
    top: 160px;
    list-style: none;
    text-align: center;
    color: var(--green);
    font-weight: 600;
    font-size: 12.5px;
    letter-spacing: 2px;
    text-transform: uppercase;
    line-height: 1.55;
  }
  .products li::before { content: "• "; }
</style>
</head>
<body>

<section class="card card--front" aria-label="Business card front">
  <p class="company"><span class="company__dot"></span>Tidewell Pumps</p>
  <div class="divider"></div>
  <div class="contact">
    <p class="contact__name">Marcus Delane</p>
    <p class="contact__role">Managing Director</p>
    <ul class="contact__list">
      <li class="contact__item">
        <svg class="contact__icon" viewBox="0 0 24 24" aria-hidden="true"><path d="M6.6 10.8a15.1 15.1 0 0 0 6.6 6.6l2.2-2.2a1 1 0 0 1 1-.25 11.4 11.4 0 0 0 3.6.57 1 1 0 0 1 1 1V20a1 1 0 0 1-1 1A17 17 0 0 1 3 4a1 1 0 0 1 1-1h3.5a1 1 0 0 1 1 1c0 1.25.2 2.45.57 3.57a1 1 0 0 1-.25 1z"/></svg>
        <span>(02) 5550 1827</span>
      </li>
      <li class="contact__item">
        <svg class="contact__icon" viewBox="0 0 24 24" aria-hidden="true"><path d="M2 5h20v14H2z M4 7v.5l8 5 8-5V7l-8 5z" fill-rule="evenodd"/></svg>
        <span>hello@tidewellpumps.com</span>
      </li>
      <li class="contact__item">
        <svg class="contact__icon" viewBox="0 0 24 24" aria-hidden="true"><path d="M12 2a10 10 0 1 0 0 20 10 10 0 0 0 0-20zm7.9 9h-3.4a15 15 0 0 0-1.3-6A8 8 0 0 1 19.9 11zM12 4c1 1.3 2.3 3.8 2.5 7h-5C9.7 7.8 11 5.3 12 4zM8.8 5a15 15 0 0 0-1.3 6H4.1A8 8 0 0 1 8.8 5zM4.1 13h3.4a15 15 0 0 0 1.3 6A8 8 0 0 1 4.1 13zM12 20c-1-1.3-2.3-3.8-2.5-7h5c-.2 3.2-1.5 5.7-2.5 7zm3.2-1a15 15 0 0 0 1.3-6h3.4a8 8 0 0 1-4.7 6z"/></svg>
        <span>www.tidewellpumps.com</span>
      </li>
      <li class="contact__item">
        <svg class="contact__icon" viewBox="0 0 24 24" aria-hidden="true"><path d="M12 2a7 7 0 0 0-7 7c0 5.2 7 13 7 13s7-7.8 7-13a7 7 0 0 0-7-7zm0 9.5a2.5 2.5 0 1 1 0-5 2.5 2.5 0 0 1 0 5z"/></svg>
        <span>27 Harlow Close,<br>Eastport NSW 2999</span>
      </li>
    </ul>
  </div>
</section>

<section class="card card--back" aria-label="Business card back">
  <p class="company"><span class="company__dot"></span>Tidewell Pumps</p>
  <p class="services"><span>Sales</span><span>/</span><span>Service</span><span>/</span><span>Repairs</span></p>
  <ul class="products">
    <li>Solar Power Systems</li>
    <li>Hot Water Systems</li>
    <li>Energy Storage / Solar Pumping</li>
    <li>Generators / Irrigation</li>
    <li>Filtration / Pumps / Tanks</li>
  </ul>
</section>

</body>
</html>
```